Business Card design for Property Developer

We need a business card design for a Melbourne based Property Developer called "Kestrel Grove Pty Ltd".

We subdivide land and onsell to builders etc.

We already have a company logo, which is attached. Also I have attached the layout requirements from the printer. We would like a 2-sided design with one side displaying our logo by itself and the other with the required info, such as name, address, tel no., email, abn etc. The card will need to be used by 4 members of staff so name and contact details should be interchangable.
Updates

If possible, can you please write "name' "job position" "phone" "email" "address" on the card but leave them so I can add the details at a later time. Thank you. Also I plan on printing with UV spot printing as a background on the card. Keep this is mind when designing.

Thanks again.

Hello designers, please do not include pics of houses, house plansĀ or construction machinery etc as we really do not like the way it looks. Thank you.

Target Market(s)

Real Estate Agents, Land Owners, Local Council Departments, Govt Bodies, other Developers etc.

Industry/Entity Type

Business

Requirements
Must have
• 2-sided design with one side displaying our logo by itself and the other with the required info, such as name, address, tel no., email, abn etc.

```html
<!DOCTYPE html>
<html lang="en">
<head>
<meta charset="utf-8">
<title>Kestrel Grove – Business Card</title>
<link href="https://fonts.googleapis.com/css2?family=Arimo:wght@400;700&family=Inter:wght@300&display=swap" rel="stylesheet">
<style>
  :root {
    --ink: #111111;
    --card-border: #6f6f6f;
    --brand-red: #c3161c;
    --brand-blue: #1f56d6;
    --plan-grey: #d4d4d4;
    --plan-light: #f4f4f4;
    --emblem-pale: #dfe5fa;
    --emblem-soft: #eef7fd;
    --paper: #ffffff;
  }
  html, body {
    margin: 0;
    padding: 0;
    width: 900px;
    height: 1200px;
    overflow: hidden;
    background: var(--paper);
  }
  .sheet {
    position: relative;
    width: 900px;
    height: 1200px;
    font-family: "Arimo", Arial, sans-serif;
    color: var(--ink);
  }
  .page-label {
    position: absolute;
    left: 0;
    width: 900px;
    text-align: center;
    font-family: "Inter", Arial, sans-serif;
    font-weight: 300;
    font-size: 44px;
    line-height: 1;
    margin: 0;
  }
  .page-label--front { top: 20px; }
  .page-label--back { top: 642px; }

  .card {
    position: absolute;
    left: 82px;
    width: 736px;
    height: 463px;
    border: 1px solid var(--card-border);
    background: var(--paper);
    overflow: hidden;
    box-sizing: border-box;
  }
  .card--front { top: 78px; }
  .card--back { top: 701px; }

  /* Front */
  .floorplan-area {
    position: absolute;
    inset: 0;
    background: linear-gradient(115deg, transparent 0 42%, var(--plan-light) 52%, var(--plan-grey) 100%);
    clip-path: polygon(52% 0, 100% 0, 100% 100%, 58% 100%, 40% 35%);
  }
  .brand {
    position: absolute;
    left: 30px;
    top: 130px;
    width: 380px;
    display: flex;
    flex-direction: column;
    align-items: center;
  }
  .brand-mark {
    width: 160px;
    height: 160px;
    border-radius: 50%;
    background: var(--brand-blue);
  }
  .brand-name {
    margin-top: 48px;
    font-family: "Arimo", Arial, sans-serif;
    font-weight: 700;
    font-size: 40px;
    letter-spacing: 1px;
    text-transform: uppercase;
    color: var(--brand-red);
    white-space: nowrap;
  }

  /* Back */
  .emblem-faint {
    position: absolute;
    left: 408px;
    top: 38px;
    width: 330px;
    height: 330px;
    border-radius: 50%;
    background: radial-gradient(circle at 60% 30%, var(--emblem-soft), var(--emblem-pale));
  }
  .holder {
    position: absolute;
    left: 38px;
    top: 60px;
  }
  .holder-name {
    margin: 0;
    font-size: 40px;
    font-weight: 700;
    line-height: 1.05;
  }
  .holder-role {
    margin: 0;
    font-size: 27px;
    font-weight: 400;
    line-height: 1.2;
  }
  .address {
    position: absolute;
    left: 38px;
    top: 216px;
    margin: 0;
    font-style: normal;
    font-size: 19px;
    line-height: 24px;
  }
  .contacts {
    position: absolute;
    left: 38px;
    top: 352px;
    margin: 0;
    padding: 0;
    list-style: none;
    font-size: 18.5px;
    line-height: 30px;
  }
  .contacts strong { font-weight: 700; }
  .abn {
    position: absolute;
    right: 20px;
    top: 418px;
    margin: 0;
    font-size: 16.5px;
  }
</style>
</head>
<body>
<main class="sheet">
  <h2 class="page-label page-label--front">Page 1</h2>
  <section class="card card--front" aria-label="Card front">
    <div class="floorplan-area" role="img" aria-label="Faint grey architectural floor plan background"></div>
    <div class="brand">
      <div class="brand-mark" aria-hidden="true"></div>
      <div class="brand-name">Kestrel Grove</div>
    </div>
  </section>

  <h2 class="page-label page-label--back">Page 2</h2>
  <section class="card card--back" aria-label="Card back">
    <div class="emblem-faint" aria-hidden="true"></div>
    <div class="holder">
      <p class="holder-name">Daniel Whitford</p>
      <p class="holder-role">Property Developer</p>
    </div>
    <address class="address">
      Unit 3 Kestrel Grove<br>
      3186 Melbourne Victoria<br>
      Australia
    </address>
    <ul class="contacts">
      <li><strong>Tel:</strong> (03) 9555 0142</li>
      <li><strong>Fax:</strong> (03) 9555 0143</li>
      <li><strong>Email:</strong> dwhitford@kestrelgrove.com.au</li>
    </ul>
    <p class="abn">ABN: 00 000 000 000</p>
  </section>
</main>
</body>
</html>
```